Flyer for Lawnmowing and gardening business

We are a lawn mowing and gardening business needing a flyer designed listing our services and business info.
The flyer should include all business information and contact details as below.

Lawn mowing
Gardening
Green waste removal
Pruning
Weeding
Vegetable Garden Creation

Phone number:0481657240

As well as the logo provided

Target Market(s)

Local people wanting someone to care for their garden.

Industry/Entity Type

Gardener

Font styles to use
Serif

Requirements
Must have
• Business Logo
• All business info and services provided. EG
• Lawn mowing
• Gardening
• Green waste removal
• Pruning
• Weeding
• Vegetable Garden Creation
• Phone number:0481657240
Nice to have
• Earthy tones, clean and simple flyer design

```html
<!DOCTYPE html>
<html lang="en">
<head>
<meta charset="utf-8">
<title>Fernvale Green – Lawn Mowing &amp; Garden Care Flyer</title>
<link rel="stylesheet" href="https://fonts.googleapis.com/css2?family=Arimo:ital,wght@0,400;0,700;1,700&family=Bitter:wght@800&display=swap">
<style>
  :root {
    --gold: #e8a21c;
    --leaf: #5a9a1c;
    --leaf-bright: #8cc63f;
    --tick-red: #d8262e;
    --soil: #4a2a12;
    --soil-light: #6b4020;
    --brand-green: #2f5d1e;
    --white: #ffffff;
  }
  * { margin: 0; padding: 0; box-sizing: border-box; }
  html, body { width: 1200px; height: 2708px; overflow: hidden; background: var(--white); }
  .flyer {
    position: relative;
    width: 1200px;
    height: 2708px;
    overflow: hidden;
    background: var(--white);
    font-family: "Arimo", Arial, sans-serif;
  }
  .lawn-backdrop {
    position: absolute; left: 0; top: 0; width: 1200px; height: 1700px;
    background:
      linear-gradient(180deg, rgba(255,255,255,0) 50%, #ffffff 92%),
      linear-gradient(180deg, #d4e6a8 0%, #a6cf5e 25%, #84b93c 50%, #b6d86e 70%, #eef6d6 100%);
  }
  .mower-photo {
    position: absolute; left: 0; top: 0; width: 960px; height: 900px;
    border-bottom-right-radius: 360px 260px;
    background: linear-gradient(160deg, #5b5f63 0%, #3aaed0 28%, #2b9cc0 52%, #43474b 74%, #6f9a38 100%);
  }
  .headline {
    position: absolute; left: 410px; top: 70px; width: 760px;
    font-family: "Bitter", Georgia, serif; font-weight: 800;
    text-align: center; line-height: 1.12;
    text-shadow: 0 3px 4px rgba(0,0,0,0.3);
  }
  .headline .line-gold { display: block; color: var(--gold); font-size: 96px; }
  .headline .line-green { display: block; color: var(--leaf); font-size: 96px; }
  .services { position: absolute; left: 44px; top: 1030px; list-style: none; }
  .services li {
    display: flex; align-items: flex-start; gap: 22px;
    color: var(--leaf); font-weight: 700; font-size: 54px; line-height: 1.08;
    margin-bottom: 26px;
  }
  .services svg { flex: none; margin-top: 8px; }
  .photo-circle {
    position: absolute; border-radius: 50%;
    border: 14px solid var(--white);
    box-shadow: 0 6px 14px rgba(0,0,0,0.28);
    z-index: 2;
  }
  .c1 { left: 600px; top: 660px;  width: 520px; height: 520px; background: linear-gradient(135deg, #7aa83a 0%, #4f7d24 45%, #6b4a2a 100%); }
  .c2 { left: 710px; top: 1140px; width: 350px; height: 350px; background: linear-gradient(150deg, #2f6a1a 0%, #5c9a2c 50%, #8fc656 100%); }
  .c3 { left: 600px; top: 1470px; width: 400px; height: 400px; background: linear-gradient(160deg, #dfe9d2 0%, #a7c866 40%, #d4609a 75%, #5e9432 100%); }
  .c4 { left: 800px; top: 1810px; width: 370px; height: 370px; background: linear-gradient(140deg, #8c6a44 0%, #6e5132 50%, #5d8f2c 100%); }
  .c5 { left: 740px; top: 2110px; width: 330px; height: 330px; background: linear-gradient(150deg, #3f7a1e 0%, #6aa83a 55%, #2a5512 100%); }
  .brand {
    position: absolute; left: 40px; top: 2040px; width: 620px; text-align: center;
    color: var(--brand-green); font-weight: 700;
  }
  .brand-name { display: block; font-size: 62px; letter-spacing: 2px; }
  .brand-tagline { display: block; font-size: 34px; margin-top: 10px; }
  .footer-swoosh { position: absolute; left: 0; top: 2280px; width: 1200px; height: 428px; z-index: 1; }
  .contact { position: absolute; left: 0; top: 2440px; width: 1200px; padding-left: 80px; z-index: 3; }
  .contact-lead { color: var(--white); font-style: italic; font-weight: 700; font-size: 44px; letter-spacing: 1px; }
  .contact-phone { color: var(--gold); font-weight: 700; font-size: 112px; line-height: 1.05; margin-top: 4px; }
  .contact-email { color: var(--white); font-weight: 700; font-size: 60px; margin-top: 4px; }
</style>
</head>
<body>
<main class="flyer">
  <div class="lawn-backdrop" role="img" aria-label="Photo of a freshly mown green lawn with garden flowers"></div>
  <div class="mower-photo" role="img" aria-label="Photo of a blue lawn mower on grass"></div>

  <h1 class="headline">
    <span class="line-gold">MAKE YOUR</span>
    <span class="line-gold">ENVIRONMENT</span>
    <span class="line-green">GREEN</span>
  </h1>

  <ul class="services">
    <li><svg width="44" height="44" viewBox="0 0 44 44"><circle cx="22" cy="22" r="21" fill="#ffffff"/><circle cx="22" cy="22" r="17" fill="#d8262e"/><path d="M13 22 l6 6 l12 -13" stroke="#fff" stroke-width="5" fill="none" stroke-linecap="round" stroke-linejoin="round"/></svg>Lawn mowing</li>
    <li><svg width="44" height="44" viewBox="0 0 44 44"><circle cx="22" cy="22" r="21" fill="#ffffff"/><circle cx="22" cy="22" r="17" fill="#d8262e"/><path d="M13 22 l6 6 l12 -13" stroke="#fff" stroke-width="5" fill="none" stroke-linecap="round" stroke-linejoin="round"/></svg>Gardening</li>
    <li><svg width="44" height="44" viewBox="0 0 44 44"><circle cx="22" cy="22" r="21" fill="#ffffff"/><circle cx="22" cy="22" r="17" fill="#d8262e"/><path d="M13 22 l6 6 l12 -13" stroke="#fff" stroke-width="5" fill="none" stroke-linecap="round" stroke-linejoin="round"/></svg><span>Green waste<br>removal</span></li>
    <li><svg width="44" height="44" viewBox="0 0 44 44"><circle cx="22" cy="22" r="21" fill="#ffffff"/><circle cx="22" cy="22" r="17" fill="#d8262e"/><path d="M13 22 l6 6 l12 -13" stroke="#fff" stroke-width="5" fill="none" stroke-linecap="round" stroke-linejoin="round"/></svg>Pruning</li>
    <li><svg width="44" height="44" viewBox="0 0 44 44"><circle cx="22" cy="22" r="21" fill="#ffffff"/><circle cx="22" cy="22" r="17" fill="#d8262e"/><path d="M13 22 l6 6 l12 -13" stroke="#fff" stroke-width="5" fill="none" stroke-linecap="round" stroke-linejoin="round"/></svg>Weeding</li>
    <li><svg width="44" height="44" viewBox="0 0 44 44"><circle cx="22" cy="22" r="21" fill="#ffffff"/><circle cx="22" cy="22" r="17" fill="#d8262e"/><path d="M13 22 l6 6 l12 -13" stroke="#fff" stroke-width="5" fill="none" stroke-linecap="round" stroke-linejoin="round"/></svg><span>Vegetable Garden<br>Creation</span></li>
  </ul>

  <div class="photo-circle c1" role="img" aria-label="Photo of gloved hands planting a seedling with a garden trowel"></div>
  <div class="photo-circle c2" role="img" aria-label="Photo of a gardener pruning a green hedge with shears"></div>
  <div class="photo-circle c3" role="img" aria-label="Photo of a spray nozzle watering pink flowers in a garden bed"></div>
  <div class="photo-circle c4" role="img" aria-label="Photo of a gloved hand pulling weeds from soil"></div>
  <div class="photo-circle c5" role="img" aria-label="Photo of a leafy green shrub"></div>

  <div class="brand">
    <span class="brand-name">FERNVALE GREEN</span>
    <span class="brand-tagline">Lawn Mowing &amp; Garden Care</span>
  </div>

  <svg class="footer-swoosh" viewBox="0 0 1200 428" preserveAspectRatio="none" aria-hidden="true">
    <defs>
      <linearGradient id="soilGradient" x1="0" y1="0" x2="0" y2="1">
        <stop offset="0" stop-color="#6b4020"/>
        <stop offset="1" stop-color="#3e220e"/>
      </linearGradient>
    </defs>
    <path d="M0 60 C 300 120, 700 110, 1200 20 L1200 428 L0 428 Z" fill="#8cc63f"/>
    <path d="M0 95 C 320 150, 720 130, 1200 60 L1200 428 L0 428 Z" fill="url(#soilGradient)"/>
  </svg>

  <section class="contact">
    <p class="contact-lead">FOR AN OBLIGATION FREE QUOTE</p>
    <p class="contact-phone">CALL: 0481657240</p>
    <p class="contact-email">Email: info@fernvalegreen.com</p>
  </section>
</main>
</body>
</html>
```